Power Point Template Design for Consulting Company
Verdant Ridge Inc.
Helping Clients Achieve Explosive Sales
Need a slide master incorporating existing logo for all regular Power Point slide layout types (title, title and content, section header, two content, comparison, title only, blank, content with caption, picture with caption)
Corporate client presentations and professional association speaking engagements
Using Power Point 2007, Windows 7.0 O/S.
Not overpowering, prefer clean white backgrounds for better projection and printing results. Verdant Ridge Inc. Logo was designed on a previous project so all files available.
logo files in all formats
business card for reference and consistency
business letterhead for reference and consistency
business stationary coor and font for reference and consistency

```html
<!DOCTYPE html>
<html lang="en">
<head>
<meta charset="utf-8">
<title>Verdant Ridge Inc. – Slide Template</title>
<link href="https://fonts.googleapis.com/css2?family=Source+Sans+3:wght@400;600;700&display=swap" rel="stylesheet">
<style>
  :root {
    --page-bg: #e9e9ea;
    --slide-bg: #ffffff;
    --brand-blue: #1e73be;
    --brand-blue-deep: #0d4f96;
    --brand-blue-light: #3d97e0;
    --swoosh-grey: #c9cbce;
    --ray-grey: #d6d7d9;
    --text-grey: #8a8c8f;
    --web-white: #ffffff;
  }
  * { box-sizing: border-box; margin: 0; padding: 0; }
  html, body {
    width: 1200px; height: 927px; overflow: hidden;
    background: var(--page-bg);
    font-family: "Source Sans 3", "Helvetica Neue", Arial, sans-serif;
  }
  .template-sheet {
    width: 1200px; height: 927px;
    display: grid;
    grid-template-columns: 500px 500px;
    grid-template-rows: 375px 375px;
    gap: 60px;
    justify-content: center;
    align-content: center;
  }
  .slide {
    position: relative;
    background: var(--slide-bg);
    overflow: hidden;
    box-shadow: 0 4px 14px rgba(0,0,0,.18);
  }
  .slide-rays {
    position: absolute; top: 0; right: 40px;
    width: 230px; height: 300px;
  }
  .slide-frame {
    position: absolute; left: 0; bottom: 0;
    width: 500px; height: 90px;
  }
  .slide-web {
    position: absolute; left: 14px; bottom: 8px;
    font-size: 10px; color: var(--web-white); letter-spacing: .2px;
  }
  /* Title slide */
  .brand-lockup {
    position: absolute; left: 34px; top: 150px;
    display: flex; align-items: center; gap: 8px;
  }
  .brand-mark {
    width: 22px; height: 22px; background: var(--brand-blue);
  }
  .brand-name {
    font-size: 15px; font-weight: 600; color: var(--brand-blue);
  }
  .presentation-title {
    position: absolute; left: 34px; top: 196px;
    font-size: 24px; font-weight: 700; color: var(--brand-blue);
  }
  .presentation-subtitle {
    position: absolute; left: 34px; top: 228px;
    font-size: 11px; color: var(--text-grey);
  }
  /* Content slide */
  .content-heading {
    position: absolute; left: 30px; top: 34px;
    font-size: 24px; font-weight: 700; color: var(--brand-blue);
  }
  .content-body {
    position: absolute; left: 30px; top: 80px; width: 300px;
    font-size: 11px; line-height: 1.45; color: var(--text-grey);
  }
  .corner-mark {
    position: absolute; right: 26px; bottom: 30px;
    width: 30px; height: 30px; background: var(--brand-blue);
  }
</style>
</head>
<body>
<main class="template-sheet">

  <!-- Title slide -->
  <section class="slide slide-title">
    <svg class="slide-rays" viewBox="0 0 230 300" role="img" aria-label="Soft grey light rays decoration">
      <defs>
        <linearGradient id="rayFadeA" x1="0" y1="0" x2="0" y2="1">
          <stop offset="0" stop-color="var(--ray-grey)" stop-opacity=".9"/>
          <stop offset="1" stop-color="var(--ray-grey)" stop-opacity="0"/>
        </linearGradient>
      </defs>
      <polygon points="60,0 200,0 120,300 100,300" fill="url(#rayFadeA)"/>
    </svg>
    <div class="brand-lockup"><span class="brand-mark"></span><span class="brand-name">Verdant Ridge Inc.</span></div>
    <h1 class="presentation-title">Name of Presentation</h1>
    <p class="presentation-subtitle">Presenter Name</p>
    <svg class="slide-frame" viewBox="0 0 500 90" preserveAspectRatio="none">
      <defs>
        <linearGradient id="bandA" x1="0" y1="0" x2="1" y2="0">
          <stop offset="0" stop-color="var(--brand-blue-deep)"/>
          <stop offset=".6" stop-color="var(--brand-blue)"/>
          <stop offset="1" stop-color="var(--brand-blue-light)"/>
        </linearGradient>
      </defs>
      <polygon points="0,56 500,30 500,48 0,66" fill="var(--swoosh-grey)"/>
      <polygon points="0,66 500,42 500,90 0,90" fill="url(#bandA)"/>
    </svg>
    <span class="slide-web">verdantridge.com</span>
  </section>

  <!-- Content slide -->
  <section class="slide slide-content">
    <svg class="slide-rays" viewBox="0 0 230 300" role="img" aria-label="Soft grey light rays decoration">
      <defs>
        <linearGradient id="rayFadeB" x1="0" y1="0" x2="0" y2="1">
          <stop offset="0" stop-color="var(--ray-grey)" stop-opacity=".9"/>
          <stop offset="1" stop-color="var(--ray-grey)" stop-opacity="0"/>
        </linearGradient>
      </defs>
      <polygon points="60,0 200,0 120,300 100,300" fill="url(#rayFadeB)"/>
    </svg>
    <h2 class="content-heading">About us</h2>
    <p class="content-body">Our firm helps sales teams grow with clear plans, steady coaching and honest numbers. We study how your buyers decide, shape a process that fits, and train people to use it every day. Clients across many fields trust us to turn quiet quarters into strong ones, and we stay close until the results hold.</p>
    <svg class="slide-frame" viewBox="0 0 500 90" preserveAspectRatio="none">
      <defs>
        <linearGradient id="bandB" x1="0" y1="0" x2="1" y2="0">
          <stop offset="0" stop-color="var(--brand-blue-deep)"/>
          <stop offset=".6" stop-color="var(--brand-blue)"/>
          <stop offset="1" stop-color="var(--brand-blue-light)"/>
        </linearGradient>
      </defs>
      <polygon points="0,56 500,30 500,48 0,66" fill="var(--swoosh-grey)"/>
      <polygon points="0,66 500,42 500,90 0,90" fill="url(#bandB)"/>
    </svg>
    <span class="corner-mark"></span>
    <span class="slide-web">verdantridge.com</span>
  </section>

  <!-- Title slide (second) -->
  <section class="slide slide-title">
    <svg class="slide-rays" viewBox="0 0 230 300" role="img" aria-label="Soft grey light rays decoration">
      <defs>
        <linearGradient id="rayFadeC" x1="0" y1="0" x2="0" y2="1">
          <stop offset="0" stop-color="var(--ray-grey)" stop-opacity=".9"/>
          <stop offset="1" stop-color="var(--ray-grey)" stop-opacity="0"/>
        </linearGradient>
      </defs>
      <polygon points="60,0 200,0 120,300 100,300" fill="url(#rayFadeC)"/>
    </svg>
    <div class="brand-lockup"><span class="brand-mark"></span><span class="brand-name">Verdant Ridge Inc.</span></div>
    <h1 class="presentation-title">Name of Presentation</h1>
    <p class="presentation-subtitle">Presenter Name</p>
    <svg class="slide-frame" viewBox="0 0 500 90" preserveAspectRatio="none">
      <defs>
        <linearGradient id="bandC" x1="0" y1="0" x2="1" y2="0">
          <stop offset="0" stop-color="var(--brand-blue-deep)"/>
          <stop offset=".6" stop-color="var(--brand-blue)"/>
          <stop offset="1" stop-color="var(--brand-blue-light)"/>
        </linearGradient>
      </defs>
      <polygon points="0,56 500,30 500,48 0,66" fill="var(--swoosh-grey)"/>
      <polygon points="0,66 500,42 500,90 0,90" fill="url(#bandC)"/>
    </svg>
    <span class="slide-web">verdantridge.com</span>
  </section>

  <!-- Content slide (second) -->
  <section class="slide slide-content">
    <svg class="slide-rays" viewBox="0 0 230 300" role="img" aria-label="Soft grey light rays decoration">
      <defs>
        <linearGradient id="rayFadeD" x1="0" y1="0" x2="0" y2="1">
          <stop offset="0" stop-color="var(--ray-grey)" stop-opacity=".9"/>
          <stop offset="1" stop-color="var(--ray-grey)" stop-opacity="0"/>
        </linearGradient>
      </defs>
      <polygon points="60,0 200,0 120,300 100,300" fill="url(#rayFadeD)"/>
    </svg>
    <h2 class="content-heading">About us</h2>
    <p class="content-body">Our firm helps sales teams grow with clear plans, steady coaching and honest numbers. We study how your buyers decide, shape a process that fits, and train people to use it every day. Clients across many fields trust us to turn quiet quarters into strong ones, and we stay close until the results hold.</p>
    <svg class="slide-frame" viewBox="0 0 500 90" preserveAspectRatio="none">
      <defs>
        <linearGradient id="bandD" x1="0" y1="0" x2="1" y2="0">
          <stop offset="0" stop-color="var(--brand-blue-deep)"/>
          <stop offset=".6" stop-color="var(--brand-blue)"/>
          <stop offset="1" stop-color="var(--brand-blue-light)"/>
        </linearGradient>
      </defs>
      <polygon points="0,56 500,30 500,48 0,66" fill="var(--swoosh-grey)"/>
      <polygon points="0,66 500,42 500,90 0,90" fill="url(#bandD)"/>
    </svg>
    <span class="corner-mark"></span>
    <span class="slide-web">verdantridge.com</span>
  </section>

</main>
</body>
</html>
```